A building General Contractor is looking for a business card design

I need a business card designed. The company "Stoneridge Framing Contractors" is a general contractor for commercial buildings and pre-engineered metal buildings.

```html
<!DOCTYPE html>
<html lang="en">
<head>
<meta charset="utf-8">
<title>Stoneridge Framing Contractors – Business Card</title>
<link href="https://fonts.googleapis.com/css2?family=Saira:wght@400;700&display=swap" rel="stylesheet">
<style>
  :root {
    --page-bg: #e9e7e4;
    --card-black: #0d0d0d;
    --band-white: #ffffff;
    --tab-grey: #e6e6e6;
    --text-white: #f4f4f4;
    --rule-grey: #5a5a5a;
  }
  html, body {
    margin: 0;
    padding: 0;
    width: 1200px;
    height: 842px;
    overflow: hidden;
    background: var(--page-bg);
    font-family: "Saira", sans-serif;
  }
  .sheet {
    width: 1200px;
    height: 842px;
    display: flex;
    align-items: center;
    justify-content: center;
    gap: 40px;
  }
  .card {
    position: relative;
    width: 540px;
    height: 308px;
    background: var(--card-black);
    box-shadow: 0 10px 30px rgba(0,0,0,0.25);
    overflow: hidden;
    color: var(--text-white);
  }
  /* Back side: contact details */
  .card-back .band {
    position: absolute;
    left: 0;
    width: 100%;
    height: 14px;
    background: var(--band-white);
  }
  .card-back .band-top { top: 22px; }
  .card-back .band-bottom { bottom: 22px; }
  .contact {
    position: absolute;
    inset: 36px 0;
    display: flex;
    flex-direction: column;
    align-items: center;
    justify-content: center;
    text-align: center;
    text-transform: uppercase;
    letter-spacing: 0.04em;
  }
  .contact-name {
    font-weight: 700;
    font-size: 19px;
    line-height: 1.1;
  }
  .contact-role {
    font-size: 12.5px;
    line-height: 1.2;
  }
  .contact-rule {
    width: 70px;
    height: 1px;
    background: var(--rule-grey);
    margin: 10px 0;
  }
  .contact-line {
    font-size: 14px;
    line-height: 1.3;
  }
  .contact-address { margin-top: 14px; }
  /* Front side: company name */
  .card-front .tab {
    position: absolute;
    width: 26px;
    height: 52px;
    background: var(--tab-grey);
  }
  .card-front .tab-left { left: 0; top: 200px; }
  .card-front .tab-right { right: 0; top: 56px; }
  .brand {
    position: absolute;
    left: 150px;
    top: 100px;
    display: flex;
    align-items: center;
    gap: 12px;
  }
  .brand-mark {
    width: 18px;
    height: 18px;
    background: var(--text-white);
    flex: none;
  }
  .brand-name {
    font-weight: 700;
    font-size: 24px;
    line-height: 1.05;
    text-transform: uppercase;
    letter-spacing: 0.03em;
    color: var(--text-white);
  }
</style>
</head>
<body>
  <main class="sheet">
    <section class="card card-back" aria-label="Business card back">
      <div class="band band-top"></div>
      <div class="contact">
        <div class="contact-name">Daniel Harlow</div>
        <div class="contact-role">Managing Director</div>
        <div class="contact-rule"></div>
        <div class="contact-line">044-555 018 240</div>
        <div class="contact-line">hello@stoneridgeframe.com</div>
        <div class="contact-line">www.stoneridgeframe.com</div>
        <div class="contact-rule"></div>
        <div class="contact-line contact-address">78, Quarry Lane Industrial Park</div>
        <div class="contact-line">38160, Northvale</div>
      </div>
      <div class="band band-bottom"></div>
    </section>

    <section class="card card-front" aria-label="Business card front">
      <div class="tab tab-right"></div>
      <div class="brand">
        <span class="brand-mark"></span>
        <span class="brand-name">Stoneridge<br>Framing<br>Contractors</span>
      </div>
      <div class="tab tab-left"></div>
    </section>
  </main>
</body>
</html>
```